Business cards and letterhead
UK size business cards/letterhead
Project: Business cards and letterhead
Business cards and letterhead - Information Technology
Creative Brief
Professional
Gareth Pellow
Director
148 Ashcombe Lane Twickenham Middlesex TW4 3QR
gareth.pellow@corvalisen.com
www.corvalisen.com
Note business card needs to be UK-sized (i.e. 85 x 55)/double sided, and the letterhead suitable for A4 paper Back of card can contain some/all of suggested text, depending upon how well it fits
ECM Consultancy Services - Project Management and Delivery - Implementation Planning - Data Conversion Management - Existing System Reviews - Software Design and Development - Test Strategy Definition and Execution

```html
<!DOCTYPE html>
<html lang="en">
<head>
<meta charset="utf-8">
<title>Corvalisen Stationery</title>
<link href="https://fonts.googleapis.com/css2?family=Open+Sans:wght@400;600;700&display=swap" rel="stylesheet">
<style>
:root{
  --stage:#000;
  --paper:#ffffff;
  --blue-dark:#0b3f66;
  --blue:#1a6aa0;
  --silver:#b9bcc0;
  --silver-light:#e4e6e8;
  --ink:#3a3d40;
  --ink-soft:#8a8e92;
  --faint:#eef0f2;
}
*{box-sizing:border-box;margin:0;padding:0}
html,body{width:1200px;height:569px;overflow:hidden;background:var(--stage)}
body{position:relative;font-family:"Open Sans",Arial,sans-serif;color:var(--ink)}
.piece{position:absolute;background:var(--paper);overflow:hidden}
.swoosh{position:absolute;left:0;top:0;width:100%}
.brand{position:absolute;display:flex;align-items:center;gap:4px;font-weight:700;color:var(--blue-dark);letter-spacing:.5px}
.brand-dot{border-radius:50%;background:var(--blue)}
.faint-mark{position:absolute;border-radius:50%;border:22px solid var(--faint)}
.head-contact{position:absolute;color:#fff;text-align:right;line-height:1.45}
.foot-line{position:absolute;left:0;width:100%;text-align:center;color:var(--ink-soft)}

/* letterhead */
.letterhead{left:34px;top:96px;width:295px;height:456px}
.letterhead .swoosh{height:72px}
.letterhead .brand{left:16px;top:16px;font-size:9px}
.letterhead .brand-dot{width:12px;height:12px}
.letterhead .head-contact{right:12px;top:8px;font-size:4.5px}
.letterhead .faint-mark{left:40px;top:190px;width:170px;height:170px}
.letterhead .foot-line{bottom:12px;font-size:4.5px}

/* fax */
.fax{left:379px;top:96px;width:293px;height:456px}
.fax .swoosh{height:72px}
.fax .brand{left:16px;top:16px;font-size:9px}
.fax .brand-dot{width:12px;height:12px}
.fax .head-contact{right:12px;top:8px;font-size:4.5px}
.fax-title{position:absolute;left:16px;top:86px;font-size:18px;font-weight:400;color:var(--ink)}
.fax-fields{position:absolute;left:16px;top:118px;width:262px;display:grid;grid-template-columns:1fr 1fr;column-gap:14px;row-gap:8px}
.fax-field{display:flex;align-items:flex-end;gap:4px;font-size:4.5px;color:var(--ink-soft);border-bottom:.6px solid var(--silver);padding-bottom:1px}
.fax-rule{position:absolute;left:16px;width:262px;height:.8px;background:var(--ink-soft)}
.fax-checks{position:absolute;left:16px;top:222px;width:262px;display:flex;justify-content:space-between}
.fax-check{display:flex;align-items:center;gap:3px;font-size:4.2px;color:var(--ink-soft)}
.fax-check i{width:6px;height:6px;border:.6px solid var(--ink-soft);display:block}
.fax .foot-line{bottom:12px;font-size:4.5px}

/* envelopes */
.env-back{left:744px;top:96px;width:432px;height:175px;background:linear-gradient(#fff,#eceef0)}
.env-back svg{position:absolute;left:0;top:0;width:100%;height:100%}
.env-mid{left:732px;top:154px;width:432px;height:158px;box-shadow:0 2px 6px rgba(0,0,0,.5)}
.env-mid .swoosh{height:60px}
.env-front{left:763px;top:194px;width:418px;height:178px;box-shadow:0 2px 8px rgba(0,0,0,.6)}
.env-front .swoosh{height:66px}
.env-front .brand{left:14px;top:14px;font-size:10px}
.env-front .brand-dot{width:14px;height:14px}
.env-address{position:absolute;left:14px;top:36px;font-size:4.5px;color:var(--ink-soft);line-height:1.45}
.env-front .faint-mark{right:20px;top:96px;width:70px;height:70px;border-width:10px}
.env-web{position:absolute;right:14px;bottom:8px;font-size:4.5px;color:var(--ink-soft)}

/* cards */
.card-front{left:782px;top:456px;width:118px;height:72px}
.card-front .swoosh{height:40px}
.card-front .brand{left:8px;top:10px;font-size:6px}
.card-front .brand-dot{width:8px;height:8px}
.card-front .head-contact{right:6px;top:5px;font-size:3.4px}
.card-front .card-lines{position:absolute;left:8px;top:44px;font-size:3.4px;color:var(--ink-soft);line-height:1.5}
.card-back{left:917px;top:425px;width:132px;height:89px}
.card-back .swoosh{height:22px}
.card-back .brand{left:8px;top:36px;font-size:6.5px}
.card-back .brand-dot{width:8px;height:8px}
.card-person{position:absolute;left:66px;top:30px;font-size:3.6px;color:var(--ink-soft);line-height:1.5}
.card-person strong{display:block;color:var(--blue-dark);font-size:4.6px;font-weight:700}
</style>
</head>
<body>

<svg width="0" height="0" style="position:absolute">
  <defs>
    <linearGradient id="band" x1="0" y1="0" x2="1" y2="0">
      <stop offset="0" stop-color="#1a6aa0"/>
      <stop offset="1" stop-color="#0b3f66"/>
    </linearGradient>
    <linearGradient id="flap" x1="0" y1="0" x2="0" y2="1">
      <stop offset="0" stop-color="#9a9da1"/>
      <stop offset="1" stop-color="#2b2d30"/>
    </linearGradient>
    <symbol id="head-swoosh" viewBox="0 0 300 72" preserveAspectRatio="none">
      <path d="M70 0 C140 40 220 50 300 58 V66 C215 60 130 46 70 0Z" fill="#b9bcc0"/>
      <path d="M96 0 H300 V52 C225 46 150 36 96 0Z" fill="url(#band)"/>
    </symbol>
  </defs>
</svg>

<section class="piece letterhead">
  <svg class="swoosh" viewBox="0 0 300 72" preserveAspectRatio="none"><use href="#head-swoosh"/></svg>
  <div class="brand"><span class="brand-dot"></span>CORVALISEN</div>
  <div class="head-contact">Tel: 020 8946 3172 · Fax: 020 8946 3173<br>gareth.pellow@corvalisen.com<br>www.corvalisen.com</div>
  <div class="faint-mark"></div>
  <p class="foot-line">148 Ashcombe Lane Twickenham Middlesex TW4 3QR</p>
</section>

<section class="piece fax">
  <svg class="swoosh" viewBox="0 0 300 72" preserveAspectRatio="none"><use href="#head-swoosh"/></svg>
  <div class="brand"><span class="brand-dot"></span>CORVALISEN</div>
  <div class="head-contact">148 Ashcombe Lane<br>Twickenham Middlesex<br>TW4 3QR</div>
  <h1 class="fax-title">FAX</h1>
  <div class="fax-fields">
    <div class="fax-field">To:</div><div class="fax-field">From:</div>
    <div class="fax-field">Fax:</div><div class="fax-field">Pages:</div>
    <div class="fax-field">Phone:</div><div class="fax-field">Date:</div>
    <div class="fax-field">Re:</div><div class="fax-field">CC:</div>
  </div>
  <div class="fax-rule" style="top:212px"></div>
  <div class="fax-checks">
    <span class="fax-check"><i></i>Urgent</span>
    <span class="fax-check"><i></i>For Review</span>
    <span class="fax-check"><i></i>Please Comment</span>
    <span class="fax-check"><i></i>Please Reply</span>
    <span class="fax-check"><i></i>Please Recycle</span>
  </div>
  <p class="foot-line">T: 020 8946 3172 · gareth.pellow@corvalisen.com · www.corvalisen.com</p>
</section>

<section class="piece env-back">
  <svg viewBox="0 0 432 175" preserveAspectRatio="none">
    <path d="M0 0 H432 L216 92Z" fill="url(#flap)"/>
  </svg>
</section>

<section class="piece env-mid">
  <svg class="swoosh" viewBox="0 0 300 72" preserveAspectRatio="none"><use href="#head-swoosh"/></svg>
</section>

<section class="piece env-front">
  <svg class="swoosh" viewBox="0 0 300 72" preserveAspectRatio="none"><use href="#head-swoosh"/></svg>
  <div class="brand"><span class="brand-dot"></span>CORVALISEN</div>
  <p class="env-address">148 Ashcombe Lane, Twickenham,<br>Middlesex TW4 3QR</p>
  <div class="faint-mark"></div>
  <p class="env-web">www.corvalisen.com</p>
</section>

<section class="piece card-front">
  <svg class="swoosh" viewBox="0 0 300 72" preserveAspectRatio="none"><use href="#head-swoosh"/></svg>
  <div class="brand"><span class="brand-dot"></span>CORVALISEN</div>
  <div class="head-contact">ECM Consultancy<br>Project Delivery</div>
  <p class="card-lines">148 Ashcombe Lane Twickenham Middlesex TW4 3QR<br>www.corvalisen.com</p>
</section>

<section class="piece card-back">
  <svg class="swoosh" viewBox="0 0 300 72" preserveAspectRatio="none"><use href="#head-swoosh"/></svg>
  <div class="brand"><span class="brand-dot"></span>CORVALISEN</div>
  <p class="card-person"><strong>Gareth Pellow</strong>Director<br>M: 07700 918 246<br>gareth.pellow@corvalisen.com<br>www.corvalisen.com</p>
</section>

</body>
</html>
```